Business Card Design for Oncology Consulting Company

We need a business card design using a logo that has already been created.

Company name is: WMBHO - Guild for Tumor Projection, Therapy and Remediation

We would also like to include the following pieces of information on the business card:
Name
Title
US Address (street, city, state, zip, country)
Email address
Website address

Target Market(s)

The target customers are physicians (oncologists, pathologists) in Greece, Iran, US, etc who would refer patients to our company for a second medical opinion/genetic counseling for cancer.

Industry/Entity Type

Business

Colors

Designer to choose colors to be used in the design.

Requirements
Must have
• Must contain logo in attached file and elements described above.

```html
<!DOCTYPE html>
<html lang="en">
<head>
<meta charset="utf-8">
<title>WMBHO Business Card</title>
<link rel="stylesheet" href="https://fonts.googleapis.com/css2?family=Open+Sans:wght@400;600&display=swap">
<style>
  :root {
    --backdrop: #8b6d49;
    --card: #ffffff;
    --card-shade: #eef0f2;
    --blue: #1f8fd0;
    --blue-deep: #1670b4;
    --blue-light: #45b3e6;
    --grey: #a9adb2;
    --text-grey: #6b6f74;
    --helix: #cfe4f1;
  }
  * { margin: 0; padding: 0; box-sizing: border-box; }
  html, body { width: 704px; height: 1200px; overflow: hidden; }
  body {
    background: var(--backdrop);
    font-family: "Open Sans", Arial, sans-serif;
    position: relative;
  }
  .card {
    position: absolute;
    left: 72px;
    width: 560px;
    height: 320px;
    background: linear-gradient(160deg, var(--card) 40%, var(--card-shade));
    overflow: hidden;
    box-shadow: 0 10px 24px rgba(0,0,0,0.35);
  }
  .card--front { top: 140px; }
  .card--back { top: 760px; }
  .card-shapes { position: absolute; inset: 0; }
  .layer { position: absolute; white-space: nowrap; }

  /* front */
  .helix-area {
    left: 20px; top: 20px; width: 190px; height: 280px;
    background: linear-gradient(120deg, rgba(207,228,241,0) 0%, var(--helix) 50%, rgba(207,228,241,0) 100%);
    opacity: 0.8;
  }
  .front-wordmark {
    left: 40px; top: 96px;
    font-size: 82px; font-weight: 600; letter-spacing: 1px;
    color: var(--blue); line-height: 1;
  }
  .front-fullname {
    right: 14px; bottom: 12px;
    font-size: 9.5px; font-weight: 600; letter-spacing: 0.3px;
    text-transform: uppercase; color: #ffffff;
  }

  /* back */
  .back-logo { left: 30px; top: 124px; display: flex; align-items: center; gap: 8px; }
  .back-wordmark { font-size: 46px; font-weight: 600; color: var(--blue); line-height: 1; letter-spacing: 1px; }
  .back-dot { width: 12px; height: 12px; border-radius: 50%; background: var(--blue-light); }
  .back-tagline {
    left: 32px; top: 186px;
    font-size: 6.5px; letter-spacing: 0.6px; text-transform: uppercase; color: var(--grey);
  }
  .address { left: 278px; top: 146px; font-size: 10px; color: var(--text-grey); line-height: 1.45; font-style: normal; }
  .divider { left: 30px; top: 180px; width: 368px; height: 1px; background: #2b2d30; }
  .pin { left: 402px; top: 169px; }
  .person { left: 32px; top: 208px; }
  .person-name { font-size: 12px; color: var(--blue); text-transform: uppercase; letter-spacing: 0.5px; }
  .person-title { font-size: 11px; color: var(--text-grey); margin-top: 2px; }
  .person-title span { display: inline-block; width: 90px; border-bottom: 1px solid var(--grey); margin-left: 2px; }
  .contact-list { list-style: none; margin-top: 6px; }
  .contact-list li { display: flex; align-items: center; gap: 7px; font-size: 10.5px; color: var(--text-grey); margin-top: 3px; }
</style>
</head>
<body>

<section class="card card--front">
  <svg class="card-shapes" viewBox="0 0 560 320" aria-hidden="true">
    <path d="M110 320 C280 300 440 200 560 20 L560 40 C450 215 300 310 170 320 Z" fill="var(--grey)" opacity="0.6"/>
    <path d="M170 320 C300 310 450 215 560 40 L560 320 Z" fill="var(--blue)"/>
    <path d="M250 320 C360 300 470 230 560 110 L560 320 Z" fill="var(--blue-deep)" opacity="0.35"/>
  </svg>
  <div class="layer helix-area" role="img" aria-label="Faint DNA double helix illustration"></div>
  <div class="layer front-wordmark">WMBHO</div>
  <div class="layer front-fullname">Guild for Tumor Projection, Therapy and Remediation</div>
</section>

<section class="card card--back">
  <svg class="card-shapes" viewBox="0 0 560 320" aria-hidden="true">
    <path d="M455 0 C405 110 410 220 470 320 L486 320 C428 220 422 110 472 0 Z" fill="var(--grey)" opacity="0.7"/>
    <path d="M472 0 C422 110 428 220 486 320 L560 320 L560 0 Z" fill="var(--blue)"/>
    <path d="M510 0 C470 120 480 230 530 320 L560 320 L560 0 Z" fill="var(--blue-deep)" opacity="0.35"/>
  </svg>
  <div class="layer back-logo">
    <span class="back-wordmark">WMBHO</span>
    <span class="back-dot"></span>
  </div>
  <div class="layer back-tagline">Guild for Tumor Projection, Therapy and Remediation</div>
  <address class="layer address">
    Your address can put here<br>Your address can put here
  </address>
  <div class="layer divider"></div>
  <svg class="layer pin" width="10" height="13" viewBox="0 0 10 13" aria-hidden="true">
    <path d="M5 0 C2.2 0 0 2.2 0 5 C0 8.5 5 13 5 13 C5 13 10 8.5 10 5 C10 2.2 7.8 0 5 0 Z" fill="var(--blue)"/>
    <circle cx="5" cy="5" r="1.8" fill="#fff"/>
  </svg>
  <div class="layer person">
    <div class="person-name">Your Name</div>
    <div class="person-title">Title<span></span></div>
    <ul class="contact-list">
      <li>
        <svg width="10" height="10" viewBox="0 0 10 10" aria-hidden="true">
          <circle cx="5" cy="5" r="4.3" fill="none" stroke="var(--blue)" stroke-width="1"/>
          <ellipse cx="5" cy="5" rx="2" ry="4.3" fill="none" stroke="var(--blue)" stroke-width="0.8"/>
          <line x1="0.7" y1="5" x2="9.3" y2="5" stroke="var(--blue)" stroke-width="0.8"/>
        </svg>
        www.yourwebsite.com
      </li>
      <li>
        <svg width="10" height="8" viewBox="0 0 10 8" aria-hidden="true">
          <rect x="0" y="0" width="10" height="8" rx="1" fill="var(--blue)"/>
          <path d="M0.8 1 L5 4.5 L9.2 1" fill="none" stroke="#fff" stroke-width="0.9"/>
        </svg>
        youremail@wmbho.org
      </li>
    </ul>
  </div>
</section>

</body>
</html>
```